DISKHAVEN: Data Rescue from hard drives

Create new web site. Our existing site is at www.filevault.com.au

The site must show that our main business is recovering data from crashed hard disks. Color theme is blue. Existing logo can be used.

I want to be able to change the images and text later.

Text could be like this:

For when you didn't make a backup...

Some information is like gold to your business. We can recover data from corrupted disks. This includes your documents, email contacts, financials, contracts, photos or records.

Diskhaven has the recovery tools, software and skills. If you have a damaged disk or files we will make our best effort to recover these for you and put them on a new disk, the Cloud, a DVD or other media.

We strongly suggest that in the event of disk damage the less that you attempt to recover files yourself, the better are our chances of getting your files back. Just turn your computer off and get the disk or the whole computer to us.

Our charges are:

•Standard recovery: $450 including GST
(no recovery= no charge)

•Additional work (if required): by arrangement

•New Media: at cost

Recovery service at no charge for computers damaged in WA Bushfires. (Offer does not include supplying free new equipment)

Please see our "Testimonials" link above for remarks by happy customers. We have been in business for nineteen years and plan on staying that way, keeping you in business.

Small business

Business

Requirements
Must have
• Must suit new Google design rules to be mobile-device-friendly.

```html
<!DOCTYPE html>
<html lang="en">
<head>
<meta charset="utf-8">
<meta name="viewport" content="width=683">
<title>Diskhaven – Data Rescue from Hard Drives</title>
<link rel="stylesheet" href="https://fonts.googleapis.com/css2?family=Arimo:wght@400;700&family=Roboto:wght@400;500&family=Roboto+Condensed&family=Roboto+Slab:wght@400&family=Ubuntu:ital@1&display=swap">
<style>
:root{
  --navy:#0b4a7e;
  --navy-deep:#0a3f6c;
  --nav-active:#8b98a6;
  --ink:#111;
  --muted:#6b6b6b;
  --link:#2f7ec0;
  --strip:#ececec;
  --copy:#7b8591;
  --white:#fff;
}
*{box-sizing:border-box;margin:0;padding:0}
html,body{width:683px;height:1200px;overflow:hidden;background:var(--white)}
body{position:relative;font-family:Arimo,Arial,sans-serif;color:var(--ink)}
h2,h3,h4{font-weight:400}
.abs{position:absolute}
.topline{left:0;top:0;width:683px;height:3px;background:#222}
.brand{left:78px;top:8px;display:flex;align-items:center;gap:10px}
.brand-dot{width:62px;height:62px;border-radius:50%;background:var(--navy)}
.brand-name{font-family:Roboto,sans-serif;font-size:22px;color:var(--navy);margin-top:-12px}
.callus{left:502px;top:22px;display:flex;align-items:center;gap:5px;font-family:Roboto,sans-serif}
.callus small{display:block;font-size:8px;color:#555}
.callus strong{display:block;font-size:12px;font-weight:400;color:#222}
.navbar{left:0;top:56px;width:683px;height:22px;background:var(--navy)}
.nav{position:absolute;left:260px;top:0;display:flex;height:22px}
.nav a{display:block;height:22px;line-height:22px;padding:0 15px;color:var(--white);font-family:"Roboto Slab",serif;font-size:8.3px;text-decoration:none;border-right:1px solid #2c6596}
.nav a.active{background:var(--nav-active);padding:0 16px}
.hero{left:0;top:78px;width:683px;height:257px;background:radial-gradient(ellipse at 30% 40%,#c9a27a 0%,#8a6141 45%,#3a271a 100%)}
.arrow{width:21px;height:21px;border-radius:50%;background:rgba(235,235,235,.9);display:flex;align-items:center;justify-content:center}
.hero-caption{left:0;top:303px;width:683px;height:32px;background:rgba(60,45,35,.55);color:var(--white);font-family:"Roboto Condensed",sans-serif;font-size:23px;text-align:center;line-height:32px}
.section-title{font-family:"Roboto Slab",serif;font-weight:400;font-size:14px;text-align:center;width:683px;left:0}
.rule{height:4px;border-top:1px solid #9fb2c6;border-bottom:1px solid #9fb2c6}
.body-text{font-size:7.5px;line-height:10.4px;text-align:center}
.about-title{top:345px;color:var(--navy)}
.about-text{left:88px;top:375px;width:508px}
.backup{left:0;top:424px;width:683px;height:143px;background:var(--navy-deep)}
.backup-title{top:438px;color:var(--white)}
.backup-text{left:80px;top:473px;width:523px;color:var(--white);font-size:7.8px}
.backup-text p{margin-bottom:5px}
.charges{left:0;top:567px;width:683px;height:186px;background:linear-gradient(135deg,#3b3b3b,#2a2623 50%,#4b4540)}
.charges-title{top:583px;color:var(--white)}
.charges-text{left:88px;top:618px;width:508px;color:var(--white)}
.charge-list{left:0;top:647px;width:683px;list-style:none;color:var(--white);font-size:9px;text-align:center}
.charge-list li{height:19px}
.cta{left:267px;top:709px;width:149px;height:19px;border:1px solid #d8e3ee;background:var(--navy);color:var(--white);font-family:"Roboto Slab",serif;font-size:9px;text-align:center;line-height:17px}
.testi-title{top:768px;color:var(--navy)}
.testi-sub{left:0;top:788px;width:683px;text-align:center;font-size:7.5px;color:var(--navy)}
.small-arrow{width:13px;height:13px;border-radius:50%;background:#e7e7e7;border:1px solid #cfcfcf}
.avatar{width:64px;height:64px;border-radius:50%;background:linear-gradient(180deg,#b9c9d6,#4a5663);border:2px solid #2f9bd6}
.quote{width:180px;font-family:Ubuntu,sans-serif;font-style:italic;font-size:7.3px;line-height:12px;color:var(--muted)}
.quote cite{display:block;margin-top:2px;font-style:normal;color:var(--link)}
.clients{left:0;top:920px;width:683px;height:56px;background:var(--strip);border-top:1px solid #ddd}
.client{top:940px;width:84px;text-align:center;font-family:Roboto,sans-serif;font-weight:500;font-size:14px;color:#555}
.footer{left:0;top:976px;width:683px;height:202px;background:linear-gradient(160deg,#474747,#333 60%,#3d3d3d)}
.contact{left:80px;top:996px;color:var(--white);font-size:7.2px;line-height:10.5px}
.contact h3{font-family:Roboto,sans-serif;font-size:9px;margin:0 0 8px 12px}
.contact-item{display:flex;gap:6px;margin-bottom:10.5px}
.contact-item svg{flex:none;width:9px;height:10px;margin-top:1px}
.footer-name{left:292px;top:1098px;font-family:Roboto,sans-serif;font-size:22px;color:#5b6f86}
.inquiry{left:432px;top:995px;width:165px;height:170px;background:rgba(120,120,120,.85);border-top:2px solid #ddd;padding:10px 8px}
.inquiry h4{display:flex;align-items:center;gap:8px;font-family:Roboto,sans-serif;font-size:12px;color:var(--white)}
.inq-icon{width:20px;height:20px;border-radius:50%;background:var(--white);display:flex;align-items:center;justify-content:center}
.inquiry p{font-size:6.5px;color:var(--white);margin:9px 0 4px}
.field{height:17px;margin:0 0 2.5px 0;padding:4px 6px;background:rgba(150,150,150,.6);color:#eee;font-size:6.5px}
.field.tall{height:29px}
.submit{margin-top:4px;width:63px;height:17px;background:var(--white);color:var(--navy);font-size:8px;font-weight:700;text-align:center;line-height:17px}
.copyright{left:0;top:1178px;width:683px;height:22px;background:var(--copy);color:var(--white);font-size:6.5px;text-align:center;line-height:22px}
</style>
</head>
<body>
<div class="abs topline"></div>

<header>
  <div class="abs brand"><span class="brand-dot"></span><span class="brand-name">Diskhaven</span></div>
  <div class="abs callus">
    <svg width="18" height="18" viewBox="0 0 18 18"><circle cx="9" cy="9" r="8" fill="none" stroke="#0b4a7e" stroke-width="1.3"/><path d="M6 5l2 0 1 2-1 1a5 5 0 0 0 2 2l1-1 2 1 0 2c-4 0-7-3-7-7z" fill="#0b4a7e"/></svg>
    <div><small>Call Us Today</small><strong>08 9555 0142</strong></div>
  </div>
</header>

<nav class="abs navbar">
  <div class="nav">
    <a class="active" href="#">Home</a><a href="#">About Us</a><a href="#">Testimonials</a><a href="#">Clients</a><a href="#">Contact Us</a>
  </div>
</nav>

<section>
  <div class="abs hero" role="img" aria-label="Close-up photo of an open hard disk drive platter and read arm"></div>
  <div class="abs arrow" style="left:30px;top:188px"><svg width="8" height="8" viewBox="0 0 8 8"><path d="M5.5 1L2.5 4l3 3" stroke="#444" stroke-width="1.6" fill="none"/></svg></div>
  <div class="abs arrow" style="left:617px;top:188px"><svg width="8" height="8" viewBox="0 0 8 8"><path d="M2.5 1l3 3-3 3" stroke="#444" stroke-width="1.6" fill="none"/></svg></div>
  <div class="abs hero-caption">Recovering Data From Crashed Hard Disks</div>
</section>

<section>
  <h2 class="abs section-title about-title">About Us</h2>
  <div class="abs rule" style="left:242px;top:362px;width:199px"></div>
  <p class="abs body-text about-text">Lorem ipsum dolor sit amet, consectetuer adipiscing elit, sed diam nonummy nibh euismod tincidunt ut laoreet dolore magna aliquam erat volutpat. Ut wisi enim ad minim veniam, quis nostrud exerci tation ullamcorper suscipit lobortis nisl ut aliquip ex ea commodo consequat. Duis autem vel eum iriure dolor in hendrerit in vulputate velit esse molestie consequat, vel illum dolore.</p>
</section>

<section>
  <div class="abs backup"></div>
  <h2 class="abs section-title backup-title">For when you didn’t make a backup...</h2>
  <div class="abs rule" style="left:206px;top:457px;width:271px;border-color:#8fa9c2"></div>
  <div class="abs body-text backup-text">
    <p>Some information is like gold to your business. We can recover data from corrupted disks.This includes your documents, email contacts, financials, contracts, photos or records.</p>
    <p>Diskhaven has the recovery tools, software and skills. If you have a damaged disk or files we will make our best effort to recover these for you and put them on a new disk, the Cloud, a DVD or other media.</p>
    <p>We strongly suggest that in the event of disk damage the less that you attempt to recover files yourself, the better are our chances of getting your files back. Just turnyour computer off and get the disk or the whole computer to us.</p>
  </div>
</section>

<section>
  <div class="abs charges" role="img" aria-label="Dim photo of small worker figurines repairing an open hard drive"></div>
  <h2 class="abs section-title charges-title">Our Charges</h2>
  <div class="abs rule" style="left:242px;top:600px;width:199px;border-color:#aaa"></div>
  <p class="abs body-text charges-text">Lorem ipsum dolor sit amet, consectetuer adipiscing elit, sed diam nonummy nibh euismod tincidunt ut laoreet dolore magna aliquam erat volutpat. Ut wisi enim ad minim veniam, quis nostrud exerci tation ullamcorper suscipit lobortis nisl ut aliquip ex ea commodo.</p>
  <ul class="abs charge-list">
    <li>• Standard recovery: $450 including GST&nbsp; (no recovery= no charge)</li>
    <li>• Additional work (if required): by arrangement</li>
    <li>• New Media: at cost</li>
  </ul>
  <div class="abs cta">Schedule Your Service Today</div>
</section>

<section>
  <h2 class="abs section-title testi-title">Client Testimonials</h2>
  <div class="abs testi-sub">See What Our Say About us</div>
  <div class="abs rule" style="left:242px;top:798px;width:199px"></div>
  <div class="abs small-arrow" style="left:55px;top:832px"></div>
  <div class="abs small-arrow" style="left:612px;top:832px"></div>
  <div class="abs avatar" role="img" aria-label="Portrait of client" style="left:74px;top:822px"></div>
  <blockquote class="abs quote" style="left:150px;top:820px">“ Lorem ipsum dolor sit amet consectetuer mingin adipisicing elitsed do eiusmod tempor incididunt ut labore eter dolore magna aliqua. Ut enim ad minim vesniam, is nostrud exercitation ullamco laboris nis ut aliquip ea commodo consequat. ”<cite>Lorem Ipsum, Director</cite></blockquote>
  <div class="abs avatar" role="img" aria-label="Portrait of client" style="left:351px;top:822px"></div>
  <blockquote class="abs quote" style="left:428px;top:820px">“ Lorem ipsum dolor sit amet consectetuer mingin adipisicing elitsed do eiusmod tempor incididunt ut labore eter dolore magna aliqua. Ut enim ad minim vesniam, is nostrud exercitation ullamco laboris nis ut aliquip ea commodo consequat. ”<cite>Lorem Ipsum, Director</cite></blockquote>
</section>

<section>
  <div class="abs clients"></div>
  <div class="abs small-arrow" style="left:55px;top:941px"></div>
  <div class="abs small-arrow" style="left:612px;top:941px"></div>
  <div class="abs client" style="left:76px">Calventa</div>
  <div class="abs client" style="left:156px">Pelmora</div>
  <div class="abs client" style="left:237px">Lindora</div>
  <div class="abs client" style="left:331px">Sarvito</div>
  <div class="abs client" style="left:411px">Pelmora</div>
  <div class="abs client" style="left:506px">Mervani</div>
</section>

<footer>
  <div class="abs footer" role="img" aria-label="Darkened street map around the office location"></div>
  <div class="abs contact">
    <h3>Contact Information</h3>
    <div class="contact-item"><svg viewBox="0 0 9 10"><path d="M4.5 0a3.3 3.3 0 0 0-3.3 3.3C1.2 6 4.5 10 4.5 10s3.3-4 3.3-6.7A3.3 3.3 0 0 0 4.5 0zm0 4.6a1.3 1.3 0 1 1 0-2.6 1.3 1.3 0 0 1 0 2.6z" fill="#fff"/></svg><div>Postal Address<br>PO Box 418, Kensington Heights, Western Australia, 6950</div></div>
    <div class="contact-item"><svg viewBox="0 0 9 10"><path d="M4.5 0a3.3 3.3 0 0 0-3.3 3.3C1.2 6 4.5 10 4.5 10s3.3-4 3.3-6.7A3.3 3.3 0 0 0 4.5 0zm0 4.6a1.3 1.3 0 1 1 0-2.6 1.3 1.3 0 0 1 0 2.6z" fill="#fff"/></svg><div>Street Address<br>14 Marlow Street, Ferndale Park, Western Australia, 6154</div></div>
    <div class="contact-item"><svg viewBox="0 0 9 10"><path d="M1 1l2 0 1 2.3-1.2 1a5 5 0 0 0 2.4 2.4l1-1.2L8.5 6.5v2C4.5 8.5 1 5 1 1z" fill="#fff"/></svg><div>Telephone<br>08 9555 0142</div></div>
    <div class="contact-item"><svg viewBox="0 0 9 10"><rect x="0.5" y="2" width="8" height="6" fill="#fff"/><path d="M0.5 2l4 3 4-3" stroke="#3b3b3b" stroke-width="0.8" fill="none"/></svg><div>Email<br>Information and Support: service@diskhaven.com.au</div></div>
    <div class="contact-item"><svg viewBox="0 0 9 10"><rect x="1" y="1" width="7" height="8" fill="#fff"/></svg><div>Social Page<br>https://www.socialpage.net/DISKHAVEN</div></div>
  </div>
  <div class="abs footer-name">Diskhaven</div>
  <form class="abs inquiry">
    <h4><span class="inq-icon"><svg width="10" height="10" viewBox="0 0 9 10"><path d="M1 1l2 0 1 2.3-1.2 1a5 5 0 0 0 2.4 2.4l1-1.2L8.5 6.5v2C4.5 8.5 1 5 1 1z" fill="#0b4a7e"/></svg></span>QUICK INQUIRY</h4>
    <p>Lorem ipsum dolor sit amet, consectetuer</p>
    <div class="field">Name</div>
    <div class="field">Email</div>
    <div class="field">Phone</div>
    <div class="field tall">Message</div>
    <div class="submit">SUBMIT</div>
  </form>
  <div class="abs copyright">Copyright © 2015 Diskhaven&nbsp; All Right Reserved</div>
</footer>
</body>
</html>
```